Various Designs

We need various designs for our new hand disinfectant dispensers that feature three extra-large windows that allow users to customize the appearance simply by changing the graphics.
Each dispenser has one window at the front and one on each side. The front window can have two different sizes. Please refer to attached zip file named Dispenser_Design_Templates.
The designs should be fresh and of high quality. Please don't just place a photo and spam me.
The design should also contain our logo (TRL Switzerland - is included in the template).
The design should further be professional enough for a medical and public setting. The dispensers will be used in hospitals, medical facilities, old pension homes, schools, restaurants, kitchens, public places etc.
We value creativity a lot!
It would be great if the dispenser features a slogan such as "Hand Hygiene Saves Lives". I have added a number of slogans at the end of this description.
Do not use dark colors such as brown. These colors do not stand for hygiene. You can use black but only in conjunction with a bright color.
The following files contain designs that I like:
- 01w
- brivandecor
- worldwide
- IMG_0137
Slogans:
- Hand Hygiene Saves Lives
- Did you wash your hands?
- Did you disinfect your hands?
- Protect Yourself and Your Patients
- Healthy Hands Start Here
- Hand Hygiene We Love... We Care... We Share...
- Clean hands prevent germs from spreading.
- Practice Good Hand Hygiene
- Save Lives: Clean Your Hands
- Save Lives: Disinfect Your Hands
- Washing Hands Saves Lives
- Wash Your Hands Please
- Be aware…..!!!!! Wash with care…..!!!!!
- Hand Hygiene Station
- Hand Hygiene Share your care, not your germs
- Good Hand Hygiene It's Critical Sanitize Wash Moisturize
- Disinfect (image of a hand)
- Clean (image of a hand)
- No Water? No Problem. Waterless Hand Rub. Keep it Handy.
- Wash your hands! If not for yourself, then do it for them.
- Practice good hygiene - it-s contagious!
- Be aware, wash with care!
- Filthy fingers forecast sickness and sadness.
- Hand Hygiene The power is in your hands
- Bury the germ, Wash your hands
- Sanitize your hands and support our clean hands initiative
- Sanitize your hands. Together we can make a difference.
- You are grand if you wash your hand.
- Holding hands feels better when they’re clean.
- Be wise wash hands often.
- Wash those germs away!!!
- Your Hands Can Be Dangerous. Disinfect them to keep germs away.
- Ten out of ten patients prefer care from clean hands.
- Safety first, disinfect and protect
- It’s universal- handwashing every patient every time!
- Infection control is in your hands.
- Make your intention prevention. Wash your hands

```html
<!DOCTYPE html>
<html lang="en">
<head>
<meta charset="utf-8">
<title>TRL Switzerland – Dispenser Window Set</title>
<link rel="stylesheet" href="https://fonts.googleapis.com/css2?family=Fredoka:wght@500;600&display=swap">
<style>
  :root {
    --page: #ffffff;
    --sun: #f4cd3a;
    --lilac: #d8c1dc;
    --lilac-soft: #efe2ee;
    --violet: #8a5aa8;
    --violet-deep: #74419a;
    --peach: #e6a981;
    --cut-line: #e0303a;
    --safe-line: #6cc46a;
  }
  * { margin: 0; padding: 0; box-sizing: border-box; }
  html, body { width: 1200px; height: 1000px; overflow: hidden; background: var(--page); }
  .canvas { position: relative; width: 1200px; height: 1000px; }
  .artwork { position: absolute; inset: 0; }
  .brand {
    position: absolute; left: 486px; top: 190px;
    display: flex; align-items: flex-end; gap: 12px;
    font-family: "Fredoka", sans-serif; font-weight: 500; color: var(--violet-deep);
  }
  .brand-name { font-size: 46px; line-height: 1; letter-spacing: 6px; }
  .brand-region { font-size: 15px; line-height: 1; margin-bottom: 16px; }
  .slogan {
    position: absolute; left: 452px; top: 302px; width: 316px;
    text-align: center;
    font-family: "Fredoka", sans-serif; font-weight: 600; font-size: 22px; line-height: 32px;
    color: var(--peach);
  }
</style>
</head>
<body>
<main class="canvas">
  <svg class="artwork" width="1200" height="1000" viewBox="0 0 1200 1000" xmlns="http://www.w3.org/2000/svg">
    <defs>
      <clipPath id="panel-left"><rect x="0" y="58" width="297" height="882"/></clipPath>
      <clipPath id="panel-front"><rect x="392" y="58" width="421" height="882"/></clipPath>
      <clipPath id="panel-right"><rect x="903" y="58" width="297" height="882"/></clipPath>
      <filter id="soft-shadow" x="-20%" y="-20%" width="140%" height="140%">
        <feDropShadow dx="0" dy="0" stdDeviation="7" flood-color="#6b6b6b" flood-opacity="0.55"/>
      </filter>
      <linearGradient id="bloom" x1="0" y1="0" x2="1" y2="1">
        <stop offset="0" stop-color="#9a6ab8"/>
        <stop offset="0.6" stop-color="#a87bbd"/>
        <stop offset="1" stop-color="#e3a98a"/>
      </linearGradient>
      <linearGradient id="bloom-faint" x1="0" y1="0" x2="1" y2="1">
        <stop offset="0" stop-color="#c7a7d6" stop-opacity="0.7"/>
        <stop offset="1" stop-color="#9a6ab8" stop-opacity="0.8"/>
      </linearGradient>
    </defs>

    <!-- Side window, left -->
    <g class="window window-side-left" clip-path="url(#panel-left)">
      <path class="wave" fill="var(--lilac)" d="M0,58 H297 V60 C230,160 140,260 0,300 Z"/>
      <path class="wave-soft" fill="var(--lilac-soft)" d="M0,300 C140,260 230,160 297,60 V110 C240,250 150,330 0,350 Z"/>
      <circle class="sun-disc" cx="170" cy="1050" r="590" fill="var(--sun)" filter="url(#soft-shadow)"/>
      <path class="flower-art" role="img" aria-label="Illustration of violet crocus flowers with peach highlights"
            fill="url(#bloom)" opacity="0.85"
            d="M60,510 L120,470 L170,520 L230,480 L270,560 L297,640 V940 H20 L40,760 L90,700 L70,600 Z"/>
      <path class="cut-line" fill="none" stroke="var(--cut-line)" stroke-width="1.5"
            d="M22,70 L280,75 Q292,78 292,92 L292,904 Q292,912 282,912 L78,912 L70,720 Q66,620 20,560 Z"/>
      <path class="safe-line" fill="none" stroke="var(--safe-line)" stroke-width="1.5"
            d="M22,88 L250,92 Q270,96 272,120 L272,884 L82,888 L74,710 Q70,620 24,556 Z"/>
      <g class="mount-holes" fill="none" stroke="var(--cut-line)" stroke-width="1.2">
        <circle cx="45" cy="78" r="5"/><circle cx="252" cy="88" r="5"/>
        <circle cx="100" cy="898" r="5"/><circle cx="265" cy="890" r="5"/>
      </g>
    </g>

    <!-- Front window -->
    <g class="window window-front" clip-path="url(#panel-front)">
      <path class="wave" fill="var(--lilac)" d="M392,58 H520 C470,66 430,70 392,72 Z"/>
      <path class="wave-soft" fill="var(--lilac-soft)" d="M392,72 C440,70 480,64 560,58 C500,140 450,250 392,295 Z"/>
      <circle class="sun-disc" cx="1259" cy="422" r="559" fill="var(--sun)" filter="url(#soft-shadow)"/>
      <circle class="sun-disc" cx="200" cy="930" r="470" fill="var(--sun)" filter="url(#soft-shadow)"/>
      <path class="flower-art" role="img" aria-label="Illustration of translucent violet crocus flowers"
            fill="url(#bloom-faint)"
            d="M470,560 L540,510 L620,540 L700,480 L790,460 L813,470 V940 H460 L470,820 L520,760 L480,700 Z"/>
      <path class="cut-line" fill="none" stroke="var(--cut-line)" stroke-width="1.5"
            d="M408,68 L798,68 L748,892 L462,892 Z"/>
      <path class="safe-line" fill="none" stroke="var(--safe-line)" stroke-width="1.5"
            d="M470,100 L740,100 Q768,102 766,135 L724,840 Q720,872 692,872 L510,872 Q484,872 482,842 L440,135 Q438,100 470,100 Z"/>
      <g class="mount-holes" fill="none" stroke="var(--cut-line)" stroke-width="1.2">
        <circle cx="433" cy="98" r="5"/><circle cx="771" cy="98" r="5"/>
        <circle cx="480" cy="866" r="5"/><circle cx="724" cy="866" r="5"/>
      </g>
    </g>

    <!-- Side window, right -->
    <g class="window window-side-right" clip-path="url(#panel-right)">
      <circle class="sun-disc" cx="1130" cy="420" r="450" fill="var(--sun)" filter="url(#soft-shadow)"/>
      <path class="flower-art" role="img" aria-label="Illustration of tall violet crocus stems and blooms"
            fill="url(#bloom)" opacity="0.85"
            d="M960,80 L1040,60 L1100,120 L1180,220 L1200,300 V700 L1140,820 L1100,940 H920 L903,860 V500 L940,420 L980,300 L950,180 Z"/>
      <path class="cut-line" fill="none" stroke="var(--cut-line)" stroke-width="1.5"
            d="M932,74 L1168,70 Q1176,72 1176,84 L1172,600 Q1150,680 1150,760 L1150,902 Q1150,912 1140,912 L920,912 Q912,912 912,902 L912,86 Q914,76 932,74 Z"/>
      <path class="safe-line" fill="none" stroke="var(--safe-line)" stroke-width="1.5"
            d="M940,88 L1172,90 L1170,600 Q1140,690 1134,770 L1134,890 L926,890 L926,100 Q928,90 940,88 Z"/>
      <g class="mount-holes" fill="none" stroke="var(--cut-line)" stroke-width="1.2">
        <circle cx="942" cy="88" r="5"/><circle cx="1150" cy="80" r="5"/>
        <circle cx="930" cy="890" r="5"/><circle cx="1096" cy="898" r="5"/>
      </g>
    </g>
  </svg>

  <div class="brand">
    <span class="brand-name">TRL</span>
    <span class="brand-region">Switzerland</span>
  </div>

  <p class="slogan">BE<br>Hygiene Serene.<br>Keep Your Hands<br>CLEAN.</p>
</main>
</body>
</html>
```